Business card and stationery design

Harbourlight Gatherings Co. is a leading event and conference design and management company.
Please view lumorahostgroup.com.au

The business cards needs to convey:
- professionalism and competency
- exclusivity
- memorable experiences and quality

The business card needs to have the following aspects:
- double sided
- Full colour CMYK
- Printed on either high gloss matt card (designer to recommend)

For the business stationery we require:
- Letterhead with top banner and bottom footer
- A thank you card design
- a with compliments slip design
- a MS powerpoint and MS publisher client presentation slide design which includes cover page and then a standard presentation page
(Note- we do NOT require an envelope design- who sends letters these days!)

The company image is using the key colours of gold, silver and black.
A black background to the business card has been used before and is preferred although we are open to options.

Target Market(s)

High end corporations and businesses that require their events and conferences to be exceptionally well designed and managed

Industry/Entity Type

Business

Contact Information for Business Card

FRONT:

Darian Whitlock
- Event and Conference Specialist

Mobile- +61 (0) 491 238 604
Office- 1300 617 482
dariannw@lumorahostgroup.com.au

Web- lumorahostgroup.com.au

BACK:

- Event and

Font styles to use
Other font styles liked:
• The logo designer used Trajan Pro Bold 3 for the font text in the logo

Requirements
Must have
• Amazing design of the following:
• - business card (double sided)
• - letterhead
• - client thank you card
• - powerpoint and publisher client presentation design files

```html
<!DOCTYPE html>
<html lang="en">
<head>
<meta charset="utf-8">
<title>Harbourlight Gatherings Co. — Business Card</title>
<link rel="stylesheet" href="https://fonts.googleapis.com/css2?family=Cinzel:wght@600;700&family=Open+Sans:wght@400&display=swap">
<style>
  :root {
    --page-bg: #d9d9d9;
    --card-dark: #0a0a0b;
    --card-mid: #202123;
    --gold: #c9a26b;
    --silver: #d4d4d4;
    --text-grey: #c4c4c4;
    --pattern-light: rgba(96, 96, 98, 0.55);
    --pattern-core: #050505;
  }
  * { margin: 0; padding: 0; box-sizing: border-box; }
  html, body {
    width: 1200px;
    height: 900px;
    overflow: hidden;
  }
  body {
    background: radial-gradient(ellipse at 50% 40%, #efefef 0%, var(--page-bg) 60%, #b5b5b5 100%);
    position: relative;
  }
  .business-card {
    position: absolute;
    left: 150px;
    top: 175px;
    width: 900px;
    height: 550px;
    background: linear-gradient(100deg, var(--card-mid) 0%, #17181a 45%, var(--card-dark) 100%);
    box-shadow: 0 18px 40px rgba(0,0,0,0.35);
    overflow: hidden;
  }
  .card-pattern {
    position: absolute;
    inset: 0;
    background:
      radial-gradient(circle at 82% 40%,
        var(--pattern-core) 0px,
        var(--pattern-core) 90px,
        rgba(60,60,62,0.35) 150px,
        var(--pattern-light) 230px,
        rgba(70,70,72,0.35) 330px,
        rgba(40,40,42,0) 420px);
    -webkit-mask-image: linear-gradient(90deg, transparent 0%, transparent 48%, #000 68%, #000 100%);
    mask-image: linear-gradient(90deg, transparent 0%, transparent 48%, #000 68%, #000 100%);
  }
  .brand {
    position: absolute;
    left: 70px;
    top: 30px;
    width: 360px;
    display: flex;
    flex-direction: column;
    align-items: center;
  }
  .brand-mark {
    width: 150px;
    height: 150px;
    border-radius: 50%;
    background: var(--silver);
  }
  .brand-name {
    margin-top: 26px;
    padding-bottom: 8px;
    font-family: "Cinzel", serif;
    font-weight: 700;
    font-size: 21px;
    letter-spacing: 0.3px;
    color: var(--silver);
    white-space: nowrap;
    border-bottom: 1px solid var(--gold);
  }
  .holder {
    position: absolute;
    left: 75px;
    top: 262px;
  }
  .holder-name {
    font-family: "Cinzel", serif;
    font-weight: 600;
    font-size: 31px;
    letter-spacing: 1px;
    color: var(--gold);
    line-height: 1.2;
  }
  .holder-title {
    margin-top: 2px;
    font-family: "Open Sans", sans-serif;
    font-size: 18px;
    letter-spacing: 0.8px;
    color: var(--text-grey);
  }
  .contact-list {
    position: absolute;
    left: 75px;
    top: 348px;
    list-style: none;
    font-family: "Open Sans", sans-serif;
    font-size: 20px;
    letter-spacing: 0.6px;
    color: var(--text-grey);
  }
  .contact-list li {
    display: flex;
    align-items: center;
    height: 34px;
  }
  .contact-icon {
    width: 18px;
    height: 18px;
    margin-right: 10px;
    fill: var(--gold);
    flex-shrink: 0;
  }
</style>
</head>
<body>
  <section class="business-card" aria-label="Business card front">
    <div class="card-pattern" role="img" aria-label="Large faint spiral of grey dots decorating the right side of the card"></div>

    <div class="brand">
      <div class="brand-mark"></div>
      <div class="brand-name">Harbourlight Gatherings Co.</div>
    </div>

    <div class="holder">
      <h1 class="holder-name">Darian Whitlock</h1>
      <p class="holder-title">Event and Conference Specialist</p>
    </div>

    <ul class="contact-list">
      <li>
        <svg class="contact-icon" viewBox="0 0 24 24" aria-hidden="true"><path d="M6.6 10.8a15.1 15.1 0 0 0 6.6 6.6l2.2-2.2a1 1 0 0 1 1-.25 11.4 11.4 0 0 0 3.6.57 1 1 0 0 1 1 1V20a1 1 0 0 1-1 1A17 17 0 0 1 3 4a1 1 0 0 1 1-1h3.5a1 1 0 0 1 1 1c0 1.25.2 2.45.57 3.57a1 1 0 0 1-.25 1z"/></svg>
        +61 (0) 491 238 604
      </li>
      <li>
        <svg class="contact-icon" viewBox="0 0 24 24" aria-hidden="true"><path d="M6.6 10.8a15.1 15.1 0 0 0 6.6 6.6l2.2-2.2a1 1 0 0 1 1-.25 11.4 11.4 0 0 0 3.6.57 1 1 0 0 1 1 1V20a1 1 0 0 1-1 1A17 17 0 0 1 3 4a1 1 0 0 1 1-1h3.5a1 1 0 0 1 1 1c0 1.25.2 2.45.57 3.57a1 1 0 0 1-.25 1z"/><path d="M14 3a7 7 0 0 1 7 7h-2a5 5 0 0 0-5-5z"/></svg>
        1300 617 482
      </li>
      <li>
        <svg class="contact-icon" viewBox="0 0 24 24" aria-hidden="true"><path d="M2 5h20v14H2z M4 7v.5l8 5 8-5V7l-8 5z" fill-rule="evenodd"/></svg>
        dariannw@lumorahostgroup.com.au
      </li>
      <li>
        <svg class="contact-icon" viewBox="0 0 24 24" aria-hidden="true"><path d="M12 2a10 10 0 1 0 0 20 10 10 0 0 0 0-20zm6.9 9h-3a15 15 0 0 0-1.3-5.6A8 8 0 0 1 18.9 11zM12 4.1c.9 1.2 1.8 3.6 1.9 6.9h-3.8c.1-3.3 1-5.7 1.9-6.9zM9.4 5.4A15 15 0 0 0 8.1 11h-3a8 8 0 0 1 4.3-5.6zM5.1 13h3a15 15 0 0 0 1.3 5.6A8 8 0 0 1 5.1 13zm6.9 6.9c-.9-1.2-1.8-3.6-1.9-6.9h3.8c-.1 3.3-1 5.7-1.9 6.9zm2.6-1.3a15 15 0 0 0 1.3-5.6h3a8 8 0 0 1-4.3 5.6z"/></svg>
        lumorahostgroup.com.au
      </li>
    </ul>
  </section>
</body>
</html>
```